Law Firm Needs Stationery Design and Business Cards

i would like some fresh new ideas for letterhead. current letterhead is attached. the bottom of the letterhead should have the same content as the bottom of the current letterhead. with the dagger (cross) symbol attached at the beginning and referenced by the two names at the top. see existing letterhead and this will make better sense.

use existing logo and content. nothing overly fancy. i like simple, classy, and refined. does not have to be same font on existing letterhead.

for envelopes, use logo and Raleigh, NC address only

Industry/Entity Type

Business

Contact Information for Business Card

Name: Gregory T. Lindqvist, Esq.

2846 Harlow Lane, Suite 417
Raleigh, NC 27694

phone 919-555-0142
fax 919-555-0187
cell 919-555-0163

www.lindqvistlegal.example
greg@lindqvistlegal.example

```html
<!DOCTYPE html>
<html lang="en">
<head>
<meta charset="utf-8">
<title>Lindqvist Legal – Business Card</title>
<link rel="stylesheet" href="https://fonts.googleapis.com/css2?family=Montserrat:wght@400;600;700&display=swap">
<style>
  :root {
    --navy: #0b2570;
    --navy-soft: #163585;
    --grey: #7c7d80;
    --paper: #f3f5f8;
    --ink: #3a3b3f;
    --backdrop: #e6e7ec;
  }
  * { margin: 0; padding: 0; box-sizing: border-box; }
  html, body { width: 1200px; height: 934px; overflow: hidden; }
  body {
    background: var(--backdrop);
    font-family: "Montserrat", "Helvetica Neue", Arial, sans-serif;
    position: relative;
  }
  .card {
    position: absolute;
    top: 312px;
    width: 540px;
    height: 309px;
    overflow: hidden;
    box-shadow: 0 2px 6px rgba(0,0,0,.12);
  }
  /* Card back: navy */
  .card--back { left: 40px; background: var(--navy); }
  .card--back .backdrop-circle {
    position: absolute; right: -40px; top: -10px;
    width: 330px; height: 330px; border-radius: 50%;
    background: var(--navy-soft); opacity: .55;
  }
  .card--back .firm-mark {
    position: absolute; left: 60px; top: 132px;
    display: flex; align-items: center; gap: 12px;
  }
  .firm-mark .dot {
    width: 30px; height: 30px; border-radius: 50%; background: var(--grey);
  }
  .firm-mark .firm-name {
    font-weight: 600; font-size: 26px; letter-spacing: 2px; text-transform: uppercase;
  }
  .card--back .firm-name { color: #ffffff; }

  /* Card front: white */
  .card--front { left: 620px; background: var(--paper); }
  .card--front .band-top { position: absolute; left: 0; top: 0; width: 100%; height: 12px; background: var(--grey); }
  .card--front .band-bottom { position: absolute; left: 0; bottom: 0; width: 100%; height: 14px; background: var(--navy); }
  .card--front .firm-mark { position: absolute; left: 34px; top: 190px; }
  .card--front .firm-name { color: var(--navy); font-size: 22px; }
  .card--front .firm-mark .dot { width: 24px; height: 24px; background: var(--navy); }

  .attorney { position: absolute; right: 26px; top: 30px; text-align: right; color: var(--ink); }
  .attorney__name {
    color: var(--navy); font-weight: 700; font-size: 15px; letter-spacing: .5px;
    text-transform: uppercase; margin-bottom: 3px;
  }
  .attorney__credential { font-size: 11px; line-height: 15px; }

  .contact {
    position: absolute; right: 26px; top: 130px; text-align: right;
    font-size: 11px; line-height: 15px; color: var(--ink);
  }
  .contact .label { color: var(--navy); font-weight: 700; }
  .contact .group { margin-bottom: 8px; }
</style>
</head>
<body>
  <section class="card card--back" aria-label="Business card, back">
    <div class="backdrop-circle"></div>
    <div class="firm-mark">
      <span class="dot"></span>
      <span class="firm-name">Lindqvist Legal</span>
    </div>
  </section>

  <section class="card card--front" aria-label="Business card, front">
    <div class="band-top"></div>
    <div class="attorney">
      <p class="attorney__name">Gregory T. Lindqvist, Esq.</p>
      <p class="attorney__credential">Licensed in NC and FL</p>
      <p class="attorney__credential">Board Certified in Civil Trial Law</p>
    </div>
    <div class="contact">
      <div class="group">
        <p><span class="label">T:</span> 919.555.0142</p>
        <p><span class="label">F:</span> 919.555.0187</p>
      </div>
      <div class="group">
        <p>www.lindqvistlegal.example</p>
        <p>greg@lindqvistlegal.example</p>
      </div>
      <div class="group">
        <p>2846 Harlow Lane, Suite 417</p>
        <p>Raleigh, NC 27694</p>
      </div>
    </div>
    <div class="firm-mark">
      <span class="dot"></span>
      <span class="firm-name">Lindqvist Legal</span>
    </div>
    <div class="band-bottom"></div>
  </section>
</body>
</html>
```